Business Card Design

we need a business card design that shows the customer what we can do for them, in pictures and words. we do tipper work of supplying recycled aggregates, soil removal from site, landscaping, demolition & groundwork and much more.(you can find photo`s and a description on our web site - dulvanhaulage.co.uk)

dulvan haulage works ltd, family business doing all aspect`s of machine & tipper lorry work.

```html
<!DOCTYPE html>
<html lang="en">
<head>
<meta charset="utf-8">
<title>Dulvan Haulage Works – Business Card</title>
<link href="https://fonts.googleapis.com/css2?family=Open+Sans:wght@400;600;700;800&display=swap" rel="stylesheet">
<style>
  :root {
    --page-bg: #e9e7e3;
    --card-white: #f7f7f5;
    --brand-blue: #3a57b0;
    --brand-blue-dark: #2f4a9e;
    --brand-red: #e0322b;
    --text-light: #ffffff;
    --text-muted: #c9d2ee;
    --photo-top: #6b6a3c;
    --photo-bottom: #9a5632;
  }
  * { margin: 0; padding: 0; box-sizing: border-box; }
  html, body {
    width: 1200px; height: 1023px; overflow: hidden;
    background: var(--page-bg);
    font-family: "Open Sans", Arial, sans-serif;
  }
  .card {
    position: absolute; left: 120px; top: 237px;
    width: 960px; height: 548px;
    background: var(--brand-blue);
    box-shadow: 0 10px 30px rgba(0,0,0,.25);
    overflow: hidden;
  }
  .card-shapes { position: absolute; inset: 0; }
  .brand {
    position: absolute; left: 34px; top: 78px;
    display: flex; align-items: center; gap: 16px;
  }
  .brand-square { width: 54px; height: 54px; background: var(--brand-red); }
  .brand-name {
    color: var(--brand-blue-dark); font-weight: 800;
    font-size: 34px; line-height: 1.1; letter-spacing: .5px;
  }
  .services {
    position: absolute; left: 10px; top: 192px; width: 420px;
    text-align: center; color: var(--brand-red);
    font-weight: 600; font-size: 16px; line-height: 1.5;
    white-space: nowrap;
  }
  .site-photo {
    position: absolute; left: 0; top: 316px; width: 406px; height: 232px;
    background: linear-gradient(180deg, var(--photo-top) 0%, var(--photo-bottom) 100%);
    clip-path: polygon(0 0, 100% 0, 93.6% 100%, 0 100%);
  }
  .holder {
    position: absolute; left: 520px; top: 100px; color: var(--text-light);
  }
  .holder-name { font-size: 30px; font-weight: 700; }
  .holder-role { font-size: 19px; color: var(--text-muted); margin-top: 2px; }
  .contacts {
    position: absolute; right: 24px; top: 250px;
    list-style: none; color: var(--text-light);
    font-size: 18px; text-align: right;
  }
  .contact { display: flex; justify-content: flex-end; align-items: flex-start; gap: 10px; margin-bottom: 8px; line-height: 1.25; }
  .contact-icon {
    flex: none; width: 20px; height: 20px; margin-top: 2px;
    background: var(--brand-red); border-radius: 3px;
    display: flex; align-items: center; justify-content: center;
  }
</style>
</head>
<body>
<article class="card">
  <svg class="card-shapes" width="960" height="548" viewBox="0 0 960 548" aria-hidden="true">
    <polygon points="0,0 440,0 380,548 0,548" fill="var(--card-white)"/>
    <polygon points="440,0 470,0 410,548 380,548" fill="var(--brand-red)"/>
  </svg>

  <div class="brand">
    <span class="brand-square"></span>
    <span class="brand-name">DULVAN<br>HAULAGE WORKS</span>
  </div>

  <p class="services">We do tipper work of supplying recycled aggregates,<br>soil removal from site, landscaping, demolition<br>and groundwork and much more</p>

  <div class="site-photo" role="img" aria-label="Photo of a crawler dozer moving soil on a groundworks site"></div>

  <div class="holder">
    <p class="holder-name">Martin Fellowes</p>
    <p class="holder-role">Demolition and Groundworks</p>
  </div>

  <ul class="contacts">
    <li class="contact"><span>Dulvan Haulage Works<br>12, Ashby Lane,Elstead<br>Farnham SURREY GU9 7QX</span>
      <span class="contact-icon"><svg width="12" height="12" viewBox="0 0 12 12"><path d="M6 1a3.5 3.5 0 0 0-3.5 3.5C2.5 7 6 11 6 11s3.5-4 3.5-6.5A3.5 3.5 0 0 0 6 1z" fill="#fff"/><circle cx="6" cy="4.5" r="1.2" fill="var(--brand-red)"/></svg></span></li>
    <li class="contact"><span>07700 900482</span>
      <span class="contact-icon"><svg width="12" height="12" viewBox="0 0 12 12"><path d="M6 1a3.5 3.5 0 0 0-3.5 3.5C2.5 7 6 11 6 11s3.5-4 3.5-6.5A3.5 3.5 0 0 0 6 1z" fill="#fff"/><circle cx="6" cy="4.5" r="1.2" fill="var(--brand-red)"/></svg></span></li>
    <li class="contact"><span>01632 960718</span>
      <span class="contact-icon"><svg width="12" height="12" viewBox="0 0 12 12"><rect x="3" y="1" width="6" height="3" fill="#fff"/><rect x="1" y="4.5" width="10" height="4.5" rx="1" fill="#fff"/><rect x="3" y="8" width="6" height="3" fill="#fff"/></svg></span></li>
    <li class="contact"><span>office@dulvanhaulage.co.uk</span>
      <span class="contact-icon"><svg width="12" height="12" viewBox="0 0 12 12"><rect x="1" y="2.5" width="10" height="7" fill="#fff"/><path d="M1 2.5l5 4 5-4" fill="none" stroke="var(--brand-red)" stroke-width="1"/></svg></span></li>
    <li class="contact"><span>www.dulvanhaulage.co.uk</span>
      <span class="contact-icon"><svg width="12" height="12" viewBox="0 0 12 12"><circle cx="6" cy="6" r="4.8" fill="none" stroke="#fff" stroke-width="1.1"/><ellipse cx="6" cy="6" rx="2" ry="4.8" fill="none" stroke="#fff" stroke-width="1"/><path d="M1.2 6h9.6" stroke="#fff" stroke-width="1"/></svg></span></li>
  </ul>
</article>
</body>
</html>
```